ADVERTISING DRESS WEBSITE

We would need a dressing highlighting the distinction Golden Basket Awards 2020 https://www.trophees-panierdore-vert.com/ This is to invite customers of Bio stores to answer an online questionnaire so to note the French organic store of their choice. At the end of the reception of all the votes we will be able to determine which are the Golden Basket Awards 2020 from the point of view of the consumers customers. The desktop skin is composed of 3 images: Desktop center size: L 1280 x H 160 px file name: dc.jpg Desktop left size: L 250 x H 1600 px file name: dl.jpg Desktop right size: L 250 x H 1600 px file name: dr.jpg Warning: for the left desktop and right desktop images, we advise you not to put important elements at 100px from the bottom, because a degraded is applied on the site (cf zones of security on the image) You can see examples of dressing on: https://www.verdoyant-hebdo.com

Target Market(s)

Specialty bio shop customers

Number of Pages Required

1 page

Requirements
Must have
• My project must illustrate the competition of Golden Basket Awards 2020

```html
<!DOCTYPE html>
<html lang="fr">
<head>
<meta charset="utf-8">
<title>Golden Basket Awards 2020 – habillage</title>
<link rel="stylesheet" href="https://fonts.googleapis.com/css2?family=Montserrat:wght@600;700;800&family=Oswald:wght@500;600&display=swap">
<style>
  :root {
    --magenta: #b80c6b;
    --magenta-bright: #d31b82;
    --green: #aed03a;
    --green-dark: #8db31e;
    --red-badge: #a8201f;
    --white: #ffffff;
    --paper: #f6f6f6;
    --bg-top: #b30b6c;
    --bg-bottom: #acd23a;
  }
  * { box-sizing: border-box; margin: 0; padding: 0; }
  html, body { width: 933px; height: 1200px; overflow: hidden; }
  body {
    position: relative;
    background: linear-gradient(200deg, var(--bg-top) 0%, #b5445a 45%, #b07d48 75%, var(--bg-bottom) 100%);
    font-family: "Montserrat", sans-serif;
  }

  /* ---------- Top banner ---------- */
  .banner {
    position: absolute; left: 110px; top: 62px; width: 714px; height: 89px;
    background: var(--white); overflow: hidden;
    box-shadow: 0 2px 6px rgba(0,0,0,.15);
  }
  .banner__foliage {
    position: absolute; right: 0; top: 0; width: 360px; height: 89px;
    background: linear-gradient(90deg, rgba(255,255,255,0) 0%, rgba(196,224,160,.55) 45%, rgba(160,200,120,.6) 100%);
  }
  .banner__seal { position: absolute; left: 0; top: 0; }
  .banner__kicker {
    position: absolute; left: 127px; top: 20px;
    font-size: 14px; font-weight: 700; color: var(--magenta-bright);
  }
  .banner__title {
    position: absolute; left: 127px; top: 36px; white-space: nowrap;
    font-size: 20px; font-weight: 700; color: var(--green);
  }
  .banner__title strong {
    font-size: 30px; font-weight: 800; color: var(--magenta); margin-left: 10px;
  }
  .banner__brand { position: absolute; left: 600px; top: 26px; width: 100px; text-align: center; }

  /* ---------- Brand lockup ---------- */
  .brand__name {
    font-family: "Oswald", sans-serif; font-weight: 500; color: var(--magenta-bright);
    text-transform: uppercase; line-height: 1.05; letter-spacing: .5px;
  }
  .banner__brand .brand__name { font-size: 18px; }

  /* ---------- Skyscrapers ---------- */
  .sky {
    position: absolute; top: 195px; width: 139px; height: 891px; overflow: hidden;
    box-shadow: 0 2px 8px rgba(0,0,0,.15);
  }
  .sky--left { left: 285px; background: var(--paper); }
  .sky--right { left: 486px; background: var(--white); }
  .sky__shapes { position: absolute; inset: 0; }
  .sky__brand { position: absolute; left: 0; width: 139px; text-align: center; }
  .sky__brand .brand__name { font-size: 28px; }

  .headline {
    position: absolute; left: 0; width: 139px; text-align: center;
    font-family: "Oswald", sans-serif; font-weight: 600; text-transform: uppercase;
  }
  .sky--left .headline { top: 226px; color: var(--magenta-bright); font-size: 16px; line-height: 33px; }
  .headline .big { font-size: 26px; line-height: 30px; display: block; }
  .sky--right .headline { top: 284px; color: var(--white); font-size: 21px; line-height: 38.5px; }

  .cta {
    position: absolute; left: 12px; width: 115px; height: 25px; border-radius: 13px;
    font-family: "Oswald", sans-serif; font-weight: 600; font-size: 10px;
    color: var(--white); text-transform: uppercase; text-align: center; line-height: 25px;
  }
  .sky--left .cta { top: 494px; background: var(--green); }
  .sky--right .cta { top: 546px; background: var(--magenta-bright); }
</style>
</head>
<body>

  <!-- Leaderboard -->
  <section class="banner">
    <div class="banner__foliage" role="img" aria-label="Feuillage vert clair en arrière-plan"></div>
    <svg class="banner__seal" width="125" height="89" viewBox="0 0 125 89" aria-hidden="true">
      <path d="M0 0 H92 C112 10 118 40 110 60 C104 76 96 84 90 89 H0 Z" fill="var(--green)"/>
      <path d="M0 0 H86 C106 12 110 42 102 62 C96 76 88 84 80 89 H0 Z" fill="var(--magenta-bright)"/>
      <circle cx="53" cy="44" r="40" fill="var(--white)"/>
      <rect x="33" y="22" width="40" height="44" rx="6" fill="var(--red-badge)"/>
    </svg>
    <p class="banner__kicker">Ils participent a</p>
    <p class="banner__title">Golden Basket Awards<strong>2020</strong></p>
    <div class="banner__brand">
      <p class="brand__name">Verdoyant<br>Hebdo</p>
    </div>
  </section>

  <!-- Left skyscraper -->
  <section class="sky sky--left">
    <svg class="sky__shapes" width="139" height="891" viewBox="0 0 139 891" aria-hidden="true">
      <defs>
        <linearGradient id="produce" x1="0" y1="0" x2="0" y2="1">
          <stop offset="0" stop-color="#f6f6f6" stop-opacity="0"/>
          <stop offset=".3" stop-color="#efe3d2" stop-opacity=".6"/>
          <stop offset=".7" stop-color="#dde9c4" stop-opacity=".6"/>
          <stop offset="1" stop-color="#f6f6f6" stop-opacity="0"/>
        </linearGradient>
      </defs>
      <rect x="0" y="120" width="139" height="420" fill="url(#produce)" role="img" aria-label="Gingembre et citrons verts en fond estompé"/>
      <rect x="0" y="0" width="139" height="48" fill="var(--green-dark)"/>
      <path d="M0 40 C30 18 60 30 90 40 C110 47 125 50 139 47 V60 H0 Z" fill="var(--magenta-bright)"/>
      <path d="M0 45 C30 24 60 36 90 46 C110 52 125 54 139 52 V70 H0 Z" fill="var(--paper)"/>
      <path d="M0 440 C15 620 60 720 139 762 V891 H0 Z" fill="var(--green)"/>
      <path d="M0 464 C20 640 70 760 139 810 V891 H0 Z" fill="var(--magenta-bright)"/>
      <path d="M0 480 C15 640 60 790 139 891 H0 Z" fill="var(--magenta)"/>
    </svg>
    <div class="sky__brand" style="top:92px">
      <p class="brand__name">Verdoyant<br>Hebdo</p>
    </div>
    <p class="headline">“Contamination<br>radioactive”<br>décelée dans<br>l’eau potable<br>de millions de<span class="big">Français</span>15467 lectures</p>
    <p class="cta">www.vote-panierdore.fr</p>
  </section>

  <!-- Right skyscraper -->
  <section class="sky sky--right">
    <svg class="sky__shapes" width="139" height="891" viewBox="0 0 139 891" aria-hidden="true">
      <defs>
        <linearGradient id="berries" x1="0" y1="0" x2="0" y2="1">
          <stop offset="0" stop-color="#ea4aa6"/>
          <stop offset="1" stop-color="#c7136f"/>
        </linearGradient>
      </defs>
      <path d="M0 280 L139 151 V891 H0 Z" fill="var(--magenta-bright)"/>
      <path d="M0 288 L139 159 V891 H0 Z" fill="var(--green)"/>
      <path d="M0 704 L139 578 V891 H0 Z" fill="var(--white)"/>
      <path d="M0 718 L139 592 V891 H0 Z" fill="url(#berries)" role="img" aria-label="Photo de fruits rouges et agrumes teintée rose"/>
    </svg>
    <div class="sky__brand" style="top:56px">
      <p class="brand__name">Verdoyant<br>Hebdo</p>
    </div>
    <p class="headline">Attention<br>aux oranges<br>et citrons<br>européens,<br>avertit<br>l’AFSE</p>
    <p class="cta">www.vote-panierdore.fr</p>
  </section>

</body>
</html>
```